Keelridge Ventures Consulting firm

I need a business card that is succint for a Brisbane based business called Keelridge Ventures Consulting Pty Ltd.
We bridge the gaps between People, Process and Technology.

We are a specialist operational excellence firm, delivering strategic consulting and business advisory services in six core capabilities, across all industries and all business lines to improve performance, efficiency, profitability, automation and scalability, for clients across Australia &New Zealand.
Updates

Hi Designers, I have uploaded the logo in 3D .png format, to assist in card design.

Target Market(s)

Project Management professionals, IT professionals, corporate and government clients managing transitioning or transformation projects.

Contact Information for Business Card

Keelridge Ventures Consulting Pty Ltd

Daniel Ostrava
Principal Consultant

mobile: +61 452 160 389
email: daniel@keelridgeventuresconsulting.com.au
webpage: www.keelridgeventuresconsulting.com

professional services: strategic advisors,

Font styles to use
Sans Serif

Requirements
Must have
• Business name: Keelridge Ventures Consulting
logo: attached
Contact person: Daniel Ostrava
Title: Principal Consultant
contact details:
mobile +61 452 160
email: daniel@KeelridgeVenturesConsulting.com.au
website: KeelridgeVenturesConsulting.com

on back side with logo include: A.B.N. 71482903165

professional services offered: Business Analysis, Strategic Advisory
Nice to have
• QR code
Should not have
• contacts picture

```html
<!DOCTYPE html>
<html lang="en">
<head>
<meta charset="utf-8">
<title>Keelridge Ventures Consulting – Business Card</title>
<link rel="stylesheet" href="https://fonts.googleapis.com/css2?family=Open+Sans:wght@400;600;700&family=Roboto+Slab:wght@700&family=PT+Serif&display=swap">
<style>
  :root {
    --stage: #1f1f1f;
    --brand-red: #e2262b;
    --brand-navy: #1d2547;
    --ink: #2b2b2b;
    --rule: #9a9a9a;
    --paper: #ffffff;
  }
  * { box-sizing: border-box; margin: 0; padding: 0; }
  html, body {
    width: 1200px; height: 1015px; overflow: hidden;
    background: var(--stage);
    font-family: "Open Sans", sans-serif;
  }
  .stage {
    width: 1200px; height: 1015px;
    display: flex; flex-direction: column; align-items: center; justify-content: center;
    gap: 60px;
  }
  .card {
    width: 700px; height: 400px; position: relative; overflow: hidden;
    box-shadow: 0 14px 30px rgba(0,0,0,.55);
  }

  /* Back side */
  .card--back { background: var(--brand-red); }
  .back-texture {
    position: absolute; inset: 0;
    background: linear-gradient(160deg, #e83036 0%, #e2262b 50%, #d21f25 100%);
  }
  .back-name {
    position: absolute; inset: 0; display: flex; align-items: center; justify-content: center;
    color: var(--paper); font-weight: 700; font-size: 26px; letter-spacing: 1px;
    text-transform: uppercase;
  }

  /* Front side */
  .card--front { background: var(--paper); }
  .brand {
    position: absolute; left: 48px; top: 160px; width: 250px;
    color: var(--brand-navy); font-weight: 700; font-size: 30px; line-height: 1.05;
    text-transform: uppercase; letter-spacing: .5px;
  }
  .divider {
    position: absolute; left: 318px; top: 80px; width: 1px; height: 170px;
    background: var(--rule);
  }
  .details { position: absolute; left: 342px; top: 78px; }
  .person-name {
    font-family: "Roboto Slab", serif; font-weight: 700; font-size: 25px;
    text-transform: uppercase; letter-spacing: .5px; line-height: 1.1;
  }
  .person-name .first { color: var(--brand-red); }
  .person-name .last { color: var(--brand-navy); }
  .person-title { color: var(--ink); font-size: 17px; margin-top: 2px; }
  .contacts { list-style: none; margin-top: 20px; }
  .contacts li {
    display: flex; align-items: center; gap: 9px;
    color: var(--ink); font-size: 14.5px; line-height: 27px; white-space: nowrap;
  }
  .contacts svg { width: 16px; height: 16px; flex: none; }
  .contacts .accent { color: var(--brand-red); }
  .navy-rule {
    position: absolute; left: 0; right: 0; top: 300px; height: 3px; background: var(--brand-navy);
  }
  .service-band {
    position: absolute; left: 0; right: 0; top: 309px; bottom: 0;
    background: var(--brand-red);
    display: flex; align-items: center; justify-content: flex-end; padding-right: 46px;
    color: var(--paper); font-family: "PT Serif", serif; font-size: 22px;
    text-transform: uppercase; letter-spacing: .5px;
  }
</style>
</head>
<body>
<main class="stage">
  <section class="card card--back" aria-label="Card back">
    <div class="back-texture" role="img" aria-label="Repeating embossed brand pattern in tones of red"></div>
    <div class="back-name">Keelridge Ventures</div>
  </section>

  <section class="card card--front" aria-label="Card front">
    <div class="brand">Keelridge<br>Ventures</div>
    <div class="divider"></div>
    <div class="details">
      <h1 class="person-name"><span class="first">Daniel</span> <span class="last">Ostrava</span></h1>
      <p class="person-title">Principal Consultant</p>
      <ul class="contacts">
        <li>
          <svg viewBox="0 0 16 16" aria-hidden="true"><rect x="3" y="1.5" width="10" height="13" rx="2" fill="none" stroke="#e2262b" stroke-width="1.8"/><line x1="6.5" y1="12" x2="9.5" y2="12" stroke="#e2262b" stroke-width="1.4"/></svg>
          <span>+61 452 160 389</span>
        </li>
        <li>
          <svg viewBox="0 0 16 16" aria-hidden="true"><rect x="1" y="3" width="14" height="10" fill="#e2262b"/><polyline points="1,3 8,9 15,3" fill="none" stroke="#fff" stroke-width="1.3"/></svg>
          <span>daniel@keelridgeventuresconsulting.com.au</span>
        </li>
        <li>
          <svg viewBox="0 0 16 16" aria-hidden="true"><g fill="none" stroke="#e2262b" stroke-width="1.3"><circle cx="8" cy="8" r="6.5"/><ellipse cx="8" cy="8" rx="3" ry="6.5"/><line x1="1.5" y1="8" x2="14.5" y2="8"/><line x1="2.5" y1="4.5" x2="13.5" y2="4.5"/><line x1="2.5" y1="11.5" x2="13.5" y2="11.5"/></g></svg>
          <span><span class="accent">www.</span>keelridgeventuresconsulting<span class="accent">.com</span></span>
        </li>
      </ul>
    </div>
    <div class="navy-rule"></div>
    <div class="service-band">Professional Services: Strategic Advisors</div>
  </section>
</main>
</body>
</html>
```